Brochure design for International Beauty Trade Show

I neee a tri-fold company products' brochure to distribute to customers at an international trade show coming soon. We have 4 main product categories- hair and skincare, facial care, Body and bath and massage oil.
The brochure needs to include at least 2 photos of the main products of each category, benefits, call to action and our company contact info ( website and phone number).

Target Market(s)

Educated and high income earners looking for all-natural,pure, 100 organic products for their beauty and personal care needs. Our products cross all racial groups/demographics and suitable for all skin types

Industry/Entity Type

Hair And Beauty

Font styles to use
Serif

Colors

Designer to choose colors to be used in the design.

Requirements
Must have
• The design must stand out as pure and luxury and at the same time be inclusive using our logo design colors- orange and blue. Also, the content must be easy to read and captivating.
• Finally if using women pictures, please include Black, white, Asian and Latina to reflect the fact that our products are suitable for all skin types.
Nice to have
• Design the brochure such that it could be printed as a poster-banner ad.
Should not have
• Cookie cutter designs are not welcome

```html
<!DOCTYPE html>
<html lang="en">
<head>
<meta charset="utf-8">
<title>Lumeaura – Trade Show Brochure</title>
<link rel="stylesheet" href="https://fonts.googleapis.com/css2?family=Oswald:wght@500&family=Montserrat:wght@400;500;600&family=Roboto+Condensed:wght@400;500&display=swap">
<style>
:root{
  --orange:#f06a0f;
  --blue:#1f8fd0;
  --ink:#3a3a3a;
  --grey:#5c5c5c;
  --stage:#000;
  --paper:#fff;
  --leaf-light:#eef4d6;
  --leaf:#9cc24a;
  --leaf-deep:#5f8f2a;
}
*{box-sizing:border-box;margin:0;padding:0}
html,body{width:960px;height:1200px;overflow:hidden;background:var(--stage)}
.sheet{position:relative;width:960px;height:1200px}
.panel{position:absolute;left:158px;width:645px;height:498px;background:var(--paper);overflow:hidden}
.panel--cover{top:86px}
.panel--products{top:625px}
.abs{position:absolute}

/* cover */
.cover-greenery{left:300px;top:0;width:345px;height:300px;
  background:radial-gradient(ellipse at 75% 30%,var(--leaf) 0%,var(--leaf-light) 55%,rgba(255,255,255,0) 80%)}
.headline{left:19px;top:28px;font-family:"Oswald",sans-serif;font-weight:500;font-size:27px;line-height:30px;letter-spacing:-.4px}
.headline .l1{color:var(--orange);display:block}
.headline .l2{color:var(--blue);display:block}
.mission{left:19px;top:102px;width:170px;font-family:"Montserrat",sans-serif;font-size:9.4px;line-height:14.7px;color:var(--grey)}
.bubble{left:14px;top:210px;width:182px;height:42px;background:var(--blue);border-radius:8px;
  color:#fff;font-family:"Montserrat",sans-serif;font-weight:500;font-size:11.2px;line-height:14.5px;padding:6px 10px}
.bubble::after{content:"";position:absolute;left:10px;bottom:-7px;border:5px solid transparent;border-top:7px solid var(--blue);border-bottom:0}
.ticks{list-style:none;font-family:"Montserrat",sans-serif;color:var(--ink)}
.ticks li{position:relative;padding-left:18px}
.ticks li::before{content:"";position:absolute;left:0;top:2px;width:10px;height:10px;border:1.3px solid var(--tick)}
.ticks li::after{content:"";position:absolute;left:3px;top:1px;width:4px;height:8px;border:solid var(--tick);border-width:0 2px 2px 0;transform:rotate(40deg)}
.range{left:19px;top:272px;font-size:10.2px;line-height:13px;--tick:var(--blue)}
.range li{margin-bottom:9px}
.order{left:240px;top:54px;width:164px;text-align:center;font-family:"Montserrat",sans-serif}
.order svg{display:block;margin:0 auto 8px}
.order .cta{color:var(--orange);font-weight:600;font-size:13px;margin-bottom:8px}
.order .line{color:var(--ink);font-weight:600;font-size:13.5px;line-height:21px}
.brand{left:470px;top:58px;display:flex;align-items:center;gap:6px;font-family:"Montserrat",sans-serif;font-weight:600;font-size:17px;color:var(--orange)}
.brand .dot{width:14px;height:14px;border-radius:50%;background:var(--blue)}
.photo{position:absolute}
.photo--model-a{left:200px;top:188px;width:200px;height:310px;border-radius:100px 100px 0 0;background:linear-gradient(180deg,#5b3a28,#a8765a 60%,#e9e2da)}
.photo--model-b{left:394px;top:194px;width:251px;height:304px;border-radius:125px 0 0 0;background:linear-gradient(160deg,#2c1c14,#d9b49c 55%,#3b2519)}

/* products panel */
.top-band{left:0;top:0;width:645px;height:160px;background:linear-gradient(90deg,#eef3e2,#b8d479 70%,#8fb544)}
.top-band-cut{left:0;top:0;width:645px;height:498px}
.photo--hair{left:0;top:0;width:178px;height:155px;background:linear-gradient(160deg,#1d120c,#7a4a32 55%,#c7946f)}
.photo--oils{left:82px;top:119px;width:104px;height:160px;border-radius:6px;background:linear-gradient(180deg,#e9e4dc,#b5641e 45%,#5a3510)}
.photo--clay{left:322px;top:239px;width:93px;height:100px;border-radius:6px;background:linear-gradient(160deg,#f4f4f1,#a9cfa6 60%,#3f8a44)}
.photo--shea{left:505px;top:44px;width:110px;height:110px;border-radius:50%;background:radial-gradient(circle,#8a6a4a,#3a2a1c 70%)}
.photo--spray{left:598px;top:351px;width:40px;height:132px;border-radius:6px;background:linear-gradient(180deg,#222,#4a3d7a 40%,#b23a3a)}
.photo--spa{left:194px;top:347px;width:224px;height:151px;border-radius:110px 110px 0 0;background:linear-gradient(180deg,#e7c3a8,#f3eee9 70%)}
.cat{font-family:"Oswald",sans-serif;font-weight:500;font-size:24px;line-height:27px;letter-spacing:-.2px}
.cat--orange{color:var(--orange)}
.cat--blue{color:var(--blue)}
.rule{height:2px}
.rule--orange{background:var(--orange)}
.rule--blue{background:var(--blue)}
.benefits{font-family:"Roboto Condensed",sans-serif;font-size:10.8px;line-height:13px;color:#222;--tick:var(--orange)}
.benefits li{margin-bottom:7.8px;padding-left:16px}
.benefits--blue{--tick:var(--blue)}
</style>
</head>
<body>
<main class="sheet">

  <section class="panel panel--cover">
    <div class="abs cover-greenery" role="img" aria-label="Bamboo stalks and soft green foliage"></div>
    <h1 class="abs headline"><span class="l1">Natural Solutions</span><span class="l2">to Forever Beauty</span></h1>
    <p class="abs mission">Our mission is to satisfy our customers by supplying them with pure, natural and 100% organic products, which make them more attractive and solve the most common skin and hair problems</p>
    <div class="abs bubble">Over 20 luxury Products<br>to choose from including:</div>
    <ul class="abs ticks range">
      <li>Argan oil</li>
      <li>Prickly Pear seed oil</li>
      <li>Carrot oil</li>
      <li>Moroccan Beldi Soap</li>
      <li>Green Clay Mask</li>
      <li>Mineral and vegetable<br>based bar soaps</li>
      <li>Shea Butter</li>
      <li>Stretch marks/vergeture oil</li>
      <li>Massage oil</li>
    </ul>
    <div class="abs order">
      <svg width="38" height="32" viewBox="0 0 38 32" aria-hidden="true">
        <rect x="5" y="1" width="28" height="22" rx="2" fill="var(--orange)"/>
        <rect x="9" y="5" width="20" height="14" fill="#fff"/>
        <path d="M17 9l5 3-2 1 2 3-1 1-2-3-2 1z" fill="var(--orange)"/>
        <path d="M1 25h36v3a3 3 0 0 1-3 3H4a3 3 0 0 1-3-3z" fill="var(--orange)"/>
      </svg>
      <p class="cta">Place your order at</p>
      <p class="line">www.lumeaura.com</p>
      <p class="line">(800) 555-0142</p>
      <p class="line">info@lumeaura.com</p>
    </div>
    <div class="abs brand"><span class="dot"></span>Lumeaura</div>
    <div class="photo photo--model-a" role="img" aria-label="Model applying cream from a jar"></div>
    <div class="photo photo--model-b" role="img" aria-label="Model with long glossy hair resting on her hand"></div>
  </section>

  <section class="panel panel--products">
    <div class="abs top-band" role="img" aria-label="Soft green leaf background"></div>
    <svg class="abs top-band-cut" viewBox="0 0 645 498" aria-hidden="true">
      <path d="M0 158 L645 66 L645 498 L0 498 Z" fill="var(--paper)"/>
      <path d="M0 153 L645 61 L645 67 L0 159 Z" fill="var(--orange)"/>
    </svg>
    <div class="photo photo--hair" role="img" aria-label="Model with voluminous curly hair"></div>
    <div class="photo photo--oils" role="img" aria-label="Three argan oil pump bottles with an oil capsule"></div>
    <div class="photo photo--shea" role="img" aria-label="Shea butter tin with shea nuts"></div>
    <div class="photo photo--clay" role="img" aria-label="Cream jar and green clay mask box"></div>
    <div class="photo photo--spa" role="img" aria-label="Woman in a towel seated after a bath"></div>
    <div class="photo photo--spray" role="img" aria-label="Massage oil spray bottle with berries"></div>

    <h2 class="abs cat cat--orange" style="left:17px;top:258px">Hair &amp;<br>Skincare</h2>
    <div class="abs rule rule--orange" style="left:17px;top:318px;width:144px"></div>
    <ul class="abs ticks benefits" style="left:21px;top:330px">
      <li>Anti-Aging, remove wrinkles</li>
      <li>Natural moisturizer</li>
      <li>Heal damaged hair or sensitive scalp</li>
      <li>Soften curly and frizzy hair</li>
      <li>Reduce sebum secretion</li>
      <li>Tone, soothe and restore luster</li>
      <li>Restore fair complexion</li>
    </ul>

    <h2 class="abs cat cat--blue" style="left:227px;top:151px">Facial Care</h2>
    <div class="abs rule rule--blue" style="left:213px;top:179px;width:160px"></div>
    <ul class="abs ticks benefits benefits--blue" style="left:229px;top:196px">
      <li>Reduce sebum secretion</li>
      <li>Eliminate toxins &amp; blemishes</li>
      <li>Tighten pores</li>
      <li>Dry pimples</li>
      <li>Remove<br>blackheads</li>
    </ul>

    <h2 class="abs cat cat--orange" style="left:441px;top:134px">Body &amp;<br>Bath Care</h2>
    <div class="abs rule rule--orange" style="left:430px;top:195px;width:162px"></div>
    <ul class="abs ticks benefits" style="left:442px;top:213px">
      <li>Purify and disinfect</li>
      <li>Fight acne</li>
      <li>Rejuvenate &amp; hydrate</li>
      <li>Promote healthy looking skin</li>
      <li>Remove dead cells</li>
    </ul>

    <h2 class="abs cat cat--blue" style="left:441px;top:326px">Massage Care</h2>
    <div class="abs rule rule--blue" style="left:430px;top:360px;width:162px"></div>
    <ul class="abs ticks benefits benefits--blue" style="left:442px;top:377px">
      <li>Relief stress and pain</li>
      <li>Fight muscle<br>contraction/tenderness</li>
      <li>Eliminate stretch marks</li>
      <li>Pure, natural undiluted</li>
    </ul>
  </section>

</main>
</body>
</html>
```